Cloud Based Internet Protection Service Business Cards

I would like a professionally designed business card. I already have a logo which I have attached.

The business is an online cloud based internet protection service aimed parents, particularly at non-technical parents and also schools.

The card should be be quite simple in its design, not to full of text and give its information in a clear and concise manner

Target Market(s)

Parents (especially non-technical parents) and also schools

Industry/Entity Type

Internet

Colors

Designer to choose colors to be used in the design.

Requirements
Should not have
• Too much text or be too cluttered. No decorative fonts, just a clear and concise font.

```html
<!DOCTYPE html>
<html lang="en">
<head>
<meta charset="utf-8">
<title>SafeNest Business Card</title>
<link href="https://fonts.googleapis.com/css2?family=Montserrat:wght@400;500;600;700&family=Open+Sans:wght@400;600&display=swap" rel="stylesheet">
<style>
  :root {
    --page: #e9ebed;
    --card-white: #ffffff;
    --brand-blue: #2a8fd0;
    --brand-light: #4fb3e6;
    --brand-navy: #1d4b60;
    --navy-deep: #173c4e;
    --text-grey: #5c6770;
    --text-dark: #2f3a42;
  }
  * { box-sizing: border-box; margin: 0; padding: 0; }
  html, body { width: 900px; height: 1200px; overflow: hidden; }
  body {
    background: var(--page);
    font-family: "Open Sans", Arial, sans-serif;
    position: relative;
  }
  .card {
    position: absolute;
    left: 70px;
    width: 760px;
    height: 434px;
    overflow: hidden;
    box-shadow: 0 6px 18px rgba(0,0,0,0.12);
  }
  .card-front { top: 110px; background: var(--card-white); }
  .card-back { top: 650px; background: var(--brand-navy); }

  .brand {
    display: flex;
    align-items: center;
    gap: 14px;
    font-family: "Montserrat", Arial, sans-serif;
    font-weight: 700;
    letter-spacing: 1px;
  }
  .brand-dot { border-radius: 50%; flex: none; }
  .card-front .brand { position: absolute; left: 44px; top: 62px; font-size: 44px; color: var(--brand-blue); }
  .card-front .brand-dot { width: 30px; height: 30px; background: var(--brand-blue); }

  .contact-list {
    position: absolute; left: 44px; top: 176px;
    list-style: none;
    font-size: 14px; color: var(--text-grey);
  }
  .contact-list li { display: flex; align-items: center; gap: 12px; height: 28px; }
  .contact-list svg { width: 15px; height: 15px; fill: var(--brand-blue); flex: none; }

  .person { position: absolute; left: 460px; top: 180px; }
  .person-name {
    font-family: "Montserrat", Arial, sans-serif;
    font-size: 26px; font-weight: 500; color: var(--brand-blue);
  }
  .person-title { font-size: 15px; color: var(--text-grey); margin-top: 4px; }

  .front-web {
    position: absolute; left: 44px; top: 330px;
    font-size: 14px; color: var(--text-dark);
  }
  .front-bands { position: absolute; left: 0; bottom: 0; width: 760px; height: 70px; }

  .card-back .brand {
    position: absolute; left: 0; right: 0; top: 170px;
    justify-content: center;
    font-size: 58px; color: var(--card-white);
  }
  .card-back .brand-dot { width: 38px; height: 38px; background: var(--card-white); }
  .back-web {
    position: absolute; right: 40px; bottom: 34px;
    font-size: 15px; color: #d5e6ef;
  }
</style>
</head>
<body>

<section class="card card-front" aria-label="Card front">
  <div class="brand"><span class="brand-dot"></span>SafeNest</div>

  <ul class="contact-list">
    <li><svg viewBox="0 0 16 16"><path d="M8 1a5 5 0 0 0-5 5c0 4 5 9 5 9s5-5 5-9a5 5 0 0 0-5-5zm0 7a2 2 0 1 1 0-4 2 2 0 0 1 0 4z"/></svg>12 Harbour Lane, Northfield</li>
    <li><svg viewBox="0 0 16 16"><path d="M8 2 1 8h2v6h4v-4h2v4h4V8h2z"/></svg>Riverton, State 40210</li>
    <li><svg viewBox="0 0 16 16"><path d="M4 1h3l1 4-2 1a9 9 0 0 0 4 4l1-2 4 1v3c0 1-1 2-2 2C6 14 2 10 2 3c0-1 1-2 2-2z"/></svg>+1 555 014 2290</li>
    <li><svg viewBox="0 0 16 16"><path d="M1 3h14v10H1zm1 1v1l6 4 6-4V4z"/></svg>contact@safenestcloud.com</li>
  </ul>

  <div class="person">
    <div class="person-name">Daniel Marsh</div>
    <div class="person-title">General Director</div>
  </div>

  <div class="front-web">www.safenestcloud.com</div>

  <svg class="front-bands" viewBox="0 0 760 70" preserveAspectRatio="none" aria-hidden="true">
    <rect x="0" y="40" width="760" height="30" fill="var(--brand-light)"/>
    <polygon points="470,40 760,40 760,70 440,70" fill="var(--brand-blue)"/>
    <polygon points="560,24 760,24 760,40 548,40" fill="var(--navy-deep)"/>
  </svg>
</section>

<section class="card card-back" aria-label="Card back">
  <div class="brand"><span class="brand-dot"></span>SafeNest</div>
  <div class="back-web">www.safenestcloud.com</div>
</section>

</body>
</html>
```